Copperleaf Motorized Shade Business Card

Hello, we've had our logo made. Now we are looking for a clean and cool looking business card. One side can just be the logo with any design elements that might look good with it. The other side will be Name, Phone Number and Email. There will not be an address on the card.

```html
<!DOCTYPE html>
<html lang="en">
<head>
<meta charset="utf-8">
<title>Copperleaf Motorized Shade Business Card</title>
<link href="https://fonts.googleapis.com/css2?family=Lato:wght@400;700;900&display=swap" rel="stylesheet">
<style>
  :root {
    --stage: #3a3b3e;
    --navy: #0e3f86;
    --navy-deep: #0b3470;
    --sky: #29a3dc;
    --sun: #f8b518;
    --paper: #ffffff;
    --ink: #33363b;
  }
  * { box-sizing: border-box; margin: 0; padding: 0; }
  html, body { width: 1200px; height: 900px; overflow: hidden; }
  body {
    background: var(--stage);
    font-family: "Lato", sans-serif;
    position: relative;
  }
  .card {
    position: absolute;
    top: 296px;
    width: 540px;
    height: 308px;
    border-radius: 22px;
    overflow: hidden;
  }
  .card-front { left: 40px; background: var(--paper); }
  .card-back { left: 620px; background: var(--navy); }

  .front-swoosh { position: absolute; inset: 0; }

  .holder { position: absolute; left: 40px; top: 34px; }
  .holder-name {
    color: var(--navy);
    font-weight: 900;
    font-size: 22px;
    letter-spacing: -0.3px;
    text-transform: uppercase;
  }
  .holder-role { color: var(--ink); font-size: 14px; margin-top: 2px; }

  .contact-list { position: absolute; left: 40px; top: 108px; list-style: none; }
  .contact-list li {
    display: flex; align-items: center; gap: 8px;
    color: var(--ink); font-size: 14px; line-height: 21px;
  }
  .contact-list svg { width: 11px; height: 11px; flex: none; }

  .brand {
    position: absolute;
    display: flex; align-items: center; gap: 12px;
  }
  .brand-square { width: 22px; height: 22px; flex: none; }
  .brand-name {
    font-weight: 900;
    text-transform: uppercase;
    line-height: 1.05;
    white-space: nowrap;
  }
  .card-front .brand { right: 36px; top: 178px; }
  .card-front .brand-square { background: var(--sun); }
  .card-front .brand-name { color: var(--navy); font-size: 22px; }

  .back-field { position: absolute; inset: 0; background: var(--navy); }
  .card-back .brand { left: 50%; top: 92px; transform: translateX(-50%); }
  .card-back .brand-square { background: var(--sun); }
  .card-back .brand-name { color: var(--paper); font-size: 30px; }
  .back-web {
    position: absolute; left: 0; right: 0; top: 206px;
    text-align: center; color: var(--paper); font-size: 16px;
  }
  .back-web span { color: var(--sun); }
</style>
</head>
<body>
  <section class="card card-front">
    <svg class="front-swoosh" viewBox="0 0 540 308" preserveAspectRatio="none" aria-hidden="true">
      <path d="M0 222 C150 250 330 292 540 300 L540 308 L0 308 Z" fill="var(--sun)"/>
      <path d="M0 234 C155 262 335 298 540 303 L540 308 L0 308 Z" fill="var(--paper)"/>
      <path d="M0 240 C160 268 340 300 540 305 L540 308 L0 308 Z" fill="var(--sky)"/>
      <path d="M0 250 C165 278 345 304 540 308 L0 308 Z" fill="var(--navy)"/>
    </svg>
    <div class="holder">
      <p class="holder-name">Dana Whitlow</p>
      <p class="holder-role">Founder &amp; CEO</p>
    </div>
    <ul class="contact-list">
      <li><svg viewBox="0 0 12 12"><circle cx="6" cy="6" r="6" fill="var(--sky)"/><path d="M4 3.2l1 1.6-.6.6a4 4 0 0 0 2.2 2.2l.6-.6 1.6 1-.6 1.1C5.6 9 3 6.4 2.9 3.8z" fill="#fff"/></svg>555-014-2277</li>
      <li><svg viewBox="0 0 12 12"><rect x="1" y="2.5" width="10" height="7" rx="1" fill="var(--sky)"/><path d="M1.5 3l4.5 3.5L10.5 3" stroke="#fff" fill="none" stroke-width="1"/></svg>info@copperleafshades.com</li>
      <li><svg viewBox="0 0 12 12"><circle cx="6" cy="6" r="5.5" fill="var(--sky)"/><path d="M.8 6h10.4M6 .5c-2.5 3-2.5 8 0 11M6 .5c2.5 3 2.5 8 0 11" stroke="#fff" fill="none" stroke-width=".8"/></svg>www.copperleafshades.com</li>
    </ul>
    <div class="brand">
      <span class="brand-square"></span>
      <p class="brand-name">Copperleaf<br>Motorized Shade</p>
    </div>
  </section>

  <section class="card card-back">
    <div class="back-field" role="img" aria-label="Faint tiled pattern of small window-shade shapes on navy"></div>
    <div class="brand">
      <span class="brand-square"></span>
      <p class="brand-name">Copperleaf<br>Motorized Shade</p>
    </div>
    <p class="back-web">www.<span>copperleafshades</span>.com</p>
  </section>
</body>
</html>
```